Veranta - Solution provider in business consulting

Veranta is a swiss based company providing solutions for developing markets. The business covers various fields of business consulting, such as supply chain, product costs, quality management and manufacturing management. The Business operates in a efficient, straight and solution oriented manner.
The final design should communicate these characteristics. Asian people as well as as western people shall identify the qualities of the company at first sight.
The customer needs business cards with a simple view but an recognizable design, printed in high quality. Engraved elements such as the globe or simple words are possible.
Available colors are: (RAL)
102/102/102
51/102/102
153/204/153
255/102/51
Font: Calibri
Industry/Entity Type
Business
Look and feel
Each slider illustrates characteristics of the customer's brand and the style your logo design should communicate.

```html
<!DOCTYPE html>
<html lang="en">
<head>
<meta charset="utf-8">
<title>Veranta – Business Card</title>
<link href="https://fonts.googleapis.com/css2?family=Carlito:wght@400;700&display=swap" rel="stylesheet">
<style>
  :root {
    --paper: #ffffff;
    --card-grey: #808080;
    --band: #f9f6fa;
    --mark-grey: #666666;
    --mark-slate: #4f5c5c;
    --web-navy: #1c1f5e;
    --ink: #111111;
    --trim: #000000;
  }
  * { margin: 0; padding: 0; box-sizing: border-box; }
  html, body {
    width: 1200px; height: 843px; overflow: hidden;
    background: var(--paper);
    font-family: "Carlito", "Calibri", sans-serif;
  }
  .canvas { position: relative; width: 1200px; height: 843px; }
  .crop-marks { position: absolute; inset: 0; }
  .crop-marks line { stroke: var(--trim); stroke-width: 1.2; }
  .card {
    position: absolute; left: 98px; top: 135px;
    width: 1002px; height: 573px;
    background: var(--card-grey);
    border-radius: 48px;
    overflow: hidden;
  }
  .brand-band {
    position: absolute; left: 158px; top: 0;
    width: 62px; height: 100%;
    background: var(--band);
  }
  .brand-mark { position: absolute; left: 0; top: 0; }
  .brand-name { font-family: "Carlito", "Calibri", sans-serif; font-size: 66px; fill: var(--mark-grey); }
  .brand-dot { fill: var(--mark-slate); }
  .web-address { font-family: "Carlito", "Calibri", sans-serif; font-size: 26px; fill: var(--web-navy); }
  .details {
    position: absolute; right: 122px; text-align: right;
    color: var(--ink); font-size: 28px; line-height: 34px;
  }
  .person { top: 85px; }
  .person .name { font-weight: 700; font-size: 29px; }
  .contact { top: 213px; line-height: 34px; }
  .contact .row { display: flex; justify-content: flex-end; align-items: center; gap: 12px; }
  .contact .row.email { margin-top: -4px; }
  .contact svg { width: 26px; height: 26px; stroke: var(--ink); fill: none; stroke-width: 2; }
  .company { top: 382px; }
</style>
</head>
<body>
<div class="canvas">
  <svg class="crop-marks" width="1200" height="843" viewBox="0 0 1200 843" aria-hidden="true">
    <line x1="84" y1="0" x2="84" y2="72"/><line x1="117" y1="33" x2="117" y2="93"/>
    <line x1="0" y1="83" x2="72" y2="83"/><line x1="35" y1="117" x2="94" y2="117"/>
    <line x1="1116" y1="0" x2="1116" y2="72"/><line x1="1083" y1="33" x2="1083" y2="93"/>
    <line x1="1128" y1="83" x2="1200" y2="83"/><line x1="1106" y1="117" x2="1165" y2="117"/>
    <line x1="84" y1="771" x2="84" y2="843"/><line x1="117" y1="750" x2="117" y2="810"/>
    <line x1="0" y1="760" x2="72" y2="760"/><line x1="35" y1="726" x2="94" y2="726"/>
    <line x1="1116" y1="771" x2="1116" y2="843"/><line x1="1083" y1="750" x2="1083" y2="810"/>
    <line x1="1128" y1="760" x2="1200" y2="760"/><line x1="1106" y1="726" x2="1165" y2="726"/>
  </svg>

  <section class="card">
    <div class="brand-band"></div>
    <svg class="brand-mark" width="400" height="573" viewBox="0 0 400 573" aria-label="Veranta">
      <circle class="brand-dot" cx="190" cy="150" r="22"/>
      <text class="brand-name" transform="translate(212 470) rotate(-90)">veranta</text>
      <text class="web-address" transform="translate(306 420) rotate(-90)">www.veranta.ch</text>
    </svg>

    <div class="details person">
      <div class="name">Marco Keller</div>
      <div class="role">CEO</div>
    </div>

    <div class="details contact">
      <div class="row">
        <svg viewBox="0 0 26 26" aria-hidden="true"><rect x="7" y="2" width="12" height="21" rx="2" transform="rotate(-15 13 13)"/><line x1="11" y1="19" x2="15" y2="18"/></svg>
        <span>+41 79 000 1234</span>
      </div>
      <div class="row">
        <svg viewBox="0 0 26 26" aria-hidden="true"><path d="M7 3 L11 8 L9 11 Q11 16 15 18 L18 16 L23 20 L20 24 Q8 22 3 7 Z" fill="#111"/></svg>
        <span>+41 71 000 5678</span>
      </div>
      <div class="row email">
        <svg viewBox="0 0 26 26" aria-hidden="true"><path d="M2 11 L13 3 L24 11 L24 23 L2 23 Z"/><path d="M2 11 L13 18 L24 11"/><path d="M2 23 L10 16 M24 23 L16 16"/></svg>
        <span>marco.keller@veranta.ch</span>
      </div>
    </div>

    <div class="details company">
      <div>Veranta GmbH</div>
      <div>Talstrasse 8</div>
      <div>9246 Niederwil</div>
      <div>Switzerland</div>
    </div>
  </section>
</div>
</body>
</html>
```